RPN FORMED

building services
decks
pergola
renovation
extensions
general building

Target Market(s)

middle to upper class

Industry/Entity Type

building

Contact Information for Business Card

my details 0438917264 tkbarrow47@mailvora.com BLD581047

Font styles to use
Serif

Colors
00AB8E
00BBA5
67D7C9
C6EFE9
E9F9F6

Requirements
Must have
• logo on the front and details on the back
Nice to have
• sharp and clean lines

```html
<!DOCTYPE html>
<html lang="en">
<head>
<meta charset="utf-8">
<title>RPN FORMED – Business Card</title>
<link rel="stylesheet" href="https://fonts.googleapis.com/css2?family=Exo+2:wght@400;600;700&display=swap">
<style>
  :root {
    --backdrop: #d9dcdc;
    --card: #1d1e20;
    --teal: #00ab8e;
    --teal-bright: #00bba5;
    --grey-text: #8d8f91;
    --grey-line: #4a4c4e;
    --accent-orange: #e29a52;
    --pattern-dark: #161719;
    --pattern-light: #3d3f42;
  }
  * { box-sizing: border-box; margin: 0; padding: 0; }
  html, body {
    width: 1200px; height: 1108px; overflow: hidden;
    background: var(--backdrop);
    font-family: "Exo 2", sans-serif;
  }
  .canvas {
    position: relative; width: 1200px; height: 1108px;
    display: flex; justify-content: center; align-items: center; gap: 60px;
  }
  .card {
    position: relative; width: 420px; height: 650px;
    background: var(--card); border-radius: 22px; overflow: hidden;
    box-shadow: 0 14px 36px rgba(0,0,0,0.28);
  }
  /* Front */
  .card-front { display: flex; flex-direction: column; align-items: center; padding: 78px 38px 0; }
  .brand { display: flex; align-items: center; gap: 14px; white-space: nowrap; }
  .brand-mark { flex: none; width: 18px; height: 18px; background: var(--accent-orange); border-radius: 3px; }
  .brand-name {
    font-weight: 700; font-size: 42px; line-height: 1.15; letter-spacing: 1px; color: var(--teal);
    white-space: nowrap;
  }
  .holder { margin-top: 66px; text-align: center; }
  .holder-name { font-weight: 700; font-size: 28px; line-height: 1.2; color: var(--teal); letter-spacing: 0.5px; white-space: nowrap; }
  .holder-role { font-size: 18px; line-height: 1.3; color: var(--grey-text); margin-top: 2px; }
  .divider { width: 140px; height: 1px; background: var(--grey-line); margin: 13px auto; }
  .contact { text-align: center; font-size: 18px; color: var(--grey-text); line-height: 1.4; white-space: nowrap; }
  .licence { text-align: center; font-size: 18px; line-height: 1.3; color: var(--teal); letter-spacing: 1px; }
  .services { display: flex; justify-content: space-between; width: 100%; margin-top: 16px; }
  .service-list { list-style: none; }
  .service-list:last-child { margin-top: 40px; }
  .service-list li {
    display: flex; align-items: center; gap: 8px; white-space: nowrap;
    font-size: 19px; color: var(--teal-bright); line-height: 1.5;
  }
  .service-list li::before {
    content: ""; flex: none; width: 12px; height: 12px; border-radius: 2px; background: var(--accent-orange);
  }
  /* Back */
  .card-back .pattern-field {
    position: absolute; inset: 0;
    background: linear-gradient(225deg, var(--pattern-light) 0%, var(--card) 45%, var(--pattern-dark) 100%);
  }
  .back-brand {
    position: absolute; left: 0; right: 0; top: 470px;
    display: flex; justify-content: center; align-items: center; gap: 10px;
  }
  .back-brand .brand-mark { width: 10px; height: 10px; border-radius: 2px; }
  .back-brand .brand-name { font-size: 30px; }
</style>
</head>
<body>
<main class="canvas">
  <section class="card card-front">
    <div class="brand">
      <span class="brand-mark"></span>
      <span class="brand-name">RPN FORMED</span>
    </div>
    <div class="holder">
      <h1 class="holder-name">MARCUS HALLORAN</h1>
      <p class="holder-role">Managing Director</p>
    </div>
    <div class="divider"></div>
    <div class="contact">
      <p>0438917264</p>
      <p>tkbarrow47@mailvora.com</p>
    </div>
    <div class="divider"></div>
    <p class="licence">BLD581047</p>
    <div class="divider"></div>
    <div class="services">
      <ul class="service-list">
        <li>Building Services</li>
        <li>Renovation</li>
        <li>General Building</li>
      </ul>
      <ul class="service-list">
        <li>Decks</li>
        <li>Pergola</li>
        <li>Extensions</li>
      </ul>
    </div>
  </section>
  <section class="card card-back">
    <div class="pattern-field" role="img" aria-label="Repeating tonal gloss pattern of the company mark across the card back"></div>
    <div class="back-brand">
      <span class="brand-mark"></span>
      <span class="brand-name">RPN FORMED</span>
    </div>
  </section>
</main>
</body>
</html>
```